Book cover: Stormy Days Survival for Kids (A5)

I have a book called Stormy Days Survival for Teens. It is a book for teenagers which gives them tips and tactics on how to survive life's challenges regarding friends, family, feelings, relationships and hard stuff in life generally. I will upload the cover of this book but you can see it on my past jobs as one of the designers her eon Pixel Bazaar did it for me.
I have a new book I've written called Stormy Days Survival for Kids. This is a parallel book to Stormy Days Survival for Teens, but it is specifically for 8 to 12 or 13 year olds, rather than for older teens.
A very important aspect of this job is that it SHOULD MATCH in some strong way - the Stormy Days Survival for Teens book. I will be selling them together, displaying them together and I want them to look like two of a pair. It might be that you use the same image as the first book but change the colour of the image so that it is bright orange and green perhaps? Or that there is another image but in the image is placed in the exact same position across the book as the first book. It needs to look like the books are by the same author.
However, I would like this one to look a bit "younger", more kid friendly. For example, a font that looks like it is for kids, or kids' writing perhaps.
I dont want to have photos on the book, and I dont think I want cartoons or drawings - because I'm not sure how this will tie in with the first book.
I want it to look modern, fresh and designed specifically for kids. The text needs to be:
Stormy Days Survival - For Kids!
Tips and ideas for 8 to 13 year olds about how to stay cool, calm and confident on even the toughest days!
The back cover is going to mostly just have the table of contents listed and a blurb, with one or two cartoons which I will supply. I am keen to pick a designer to just do the front cover first and will ask them to do the back cover later.
UPDATED: I have attached three files with fonts that I like.

```html
<!DOCTYPE html>
<html lang="en">
<head>
<meta charset="utf-8">
<title>Stormy Days Survival for Kids – Front Cover</title>
<link href="https://fonts.googleapis.com/css2?family=Cabin+Sketch:wght@700&family=Permanent+Marker&family=Architects+Daughter&display=swap" rel="stylesheet">
<style>
  :root {
    --paper: #ffffff;
    --ink: #0a0a0a;
    --orange: #f7941d;
    --frame: #3a3a3a;
  }
  html, body {
    margin: 0;
    padding: 0;
    width: 827px;
    height: 1200px;
    overflow: hidden;
    background: var(--paper);
  }
  .cover {
    position: relative;
    width: 827px;
    height: 1200px;
    background: var(--paper);
    color: var(--ink);
  }
  .cover__frame {
    position: absolute;
    left: 19px;
    top: 14px;
    width: 789px;
    height: 1172px;
    border: 1.5px solid var(--frame);
    box-sizing: border-box;
  }
  .title {
    margin: 0;
    font-family: "Cabin Sketch", "Permanent Marker", sans-serif;
    font-weight: 700;
    color: var(--ink);
  }
  .title__line {
    position: absolute;
    white-space: nowrap;
    line-height: 1;
  }
  .title__line--one { left: 62px; top: 56px; font-size: 84px; letter-spacing: 3px; }
  .title__line--two { left: 112px; top: 146px; font-size: 72px; letter-spacing: 2px; }
  .title__line--three { left: 336px; top: 236px; font-size: 86px; letter-spacing: 4px; }
  .tagline {
    position: absolute;
    left: 0;
    top: 340px;
    width: 827px;
    margin: 0;
    font-family: "Architects Daughter", sans-serif;
    font-size: 21px;
    line-height: 27px;
    color: var(--ink);
  }
  .tagline__line { display: block; white-space: nowrap; }
  .tagline__line--one { padding-left: 192px; }
  .tagline__line--two { padding-left: 94px; }
  .family-art {
    position: absolute;
    left: 97px;
    top: 502px;
    width: 643px;
    height: 405px;
  }
  .credits {
    position: absolute;
    left: 0;
    top: 994px;
    width: 827px;
    font-family: "Architects Daughter", sans-serif;
    color: var(--ink);
  }
  .credits__author {
    margin: 0 0 0 444px;
    font-size: 29px;
    letter-spacing: 2px;
    line-height: 38px;
    font-weight: 700;
  }
  .credits__role {
    margin: 6px 0 0 414px;
    font-size: 31px;
    line-height: 42px;
    font-weight: 700;
  }
  .credits__illustrator {
    margin: 22px 0 0 444px;
    font-size: 18px;
    letter-spacing: 1px;
  }
</style>
</head>
<body>
  <main class="cover">
    <div class="cover__frame"></div>

    <h1 class="title">
      <span class="title__line title__line--one">STORMY</span>
      <span class="title__line title__line--two">DAYS SURVIVAL</span>
      <span class="title__line title__line--three">For Kids</span>
    </h1>

    <p class="tagline">
      <span class="tagline__line tagline__line--one">Tips and ideas for 8 to 13 year olds</span>
      <span class="tagline__line tagline__line--two">on how to stay cool, calm and confident in tough times.</span>
    </p>

    <svg class="family-art" viewBox="0 0 643 405" role="img" aria-label="Pictogram family of four: a tall black father figure, a small orange girl, a small black boy and a tall orange mother figure standing in a row">
      <defs>
        <linearGradient id="family-tones" x1="0" y1="0" x2="1" y2="0">
          <stop offset="0" stop-color="#0a0a0a"/>
          <stop offset="0.35" stop-color="#f7941d"/>
          <stop offset="0.65" stop-color="#0a0a0a"/>
          <stop offset="1" stop-color="#f7941d"/>
        </linearGradient>
      </defs>
      <rect x="0" y="0" width="643" height="405" fill="url(#family-tones)"/>
    </svg>

    <section class="credits">
      <p class="credits__author">MARLENE TOBIN</p>
      <p class="credits__role">clinical psychologist</p>
      <p class="credits__illustrator">illustrated by: Oscar Delray</p>
    </section>
  </main>
</body>
</html>
```